Launching a new real estate agency in Monaco

Hello, I am opening a new real estate agency in Monaco. For the purpose of my activity, in order to be known quickly among a fierce competition I need an advertising campaign that will be broadcast in local magazines, newspapers, paper board, etc.

You will find example of pictures of Monaco on which I have the rights and my logo. You can always pick other images that I can buy if the price is reasonable for a commercial use (<200 $)

Please respect the color code.

I wish you good luck and look forward to give you my feedbacks

Reason: Only few projects posted were respecting the brief and of quality. Hoping to receive more in coming days

Target Market(s)

International high-end clientele of all ages, all genders.

Industry/Entity Type

Real Estate Agent

Font styles to use
Serif

Requirements
Must have
• 1/ My logo
• 2/ This message "Un nouveau regard sur l'immobilier" means in English a fresh look at real estate or new eyes on real-estate.
• 3/ My address: 14 rue des Orvilles, Passage Marcellin, 98 000 Monaco
• 4/ Phone number: +377.93.48.25.71
• 5/ Website: www.brunor-agency.com.
• 6/ Format: Files should be easily adjustable but I'd like a vertical display to fit easily in Magazines, Poster and billboard. So please work in high resolution !
Nice to have
• Please think about your design in accordance with the message I want to display.
Should not have
• A simple poster with a picture of Monaco that does not take into consideration the message of the advertisement, "Un nouveau regard sur l'immobilier" which means in english, new eyes on real-estate or a new look at real-estate, or new vision at real-estate.

```html
<!DOCTYPE html>
<html lang="fr">
<head>
<meta charset="UTF-8">
<title>Brunor Agency – Un nouveau regard sur l'immobilier</title>
<link href="https://fonts.googleapis.com/css2?family=Roboto:wght@400;500;700&display=swap" rel="stylesheet">
<style>
  :root {
    --navy: #1b2a3e;
    --cyan: #3bb2cf;
    --copper: #d9a48c;
    --light: #d7dadf;
    --icon-bg: #c4c8cd;
    --sky-top: #c9ccd8;
    --sky-mid: #b9b6c9;
    --land: #6f8a5a;
    --sea: #47b9cc;
    --sea-deep: #3aa5bd;
  }
  * { margin: 0; padding: 0; box-sizing: border-box; }
  html, body { width: 873px; height: 1200px; overflow: hidden; background: var(--navy); }
  .poster {
    position: relative;
    width: 873px;
    height: 1200px;
    background: var(--navy);
    font-family: "Roboto", Arial, sans-serif;
    overflow: hidden;
  }
  .hero-photo {
    position: absolute;
    left: 0; top: 0;
    width: 873px; height: 620px;
    background:
      linear-gradient(180deg,
        var(--sky-top) 0%,
        var(--sky-mid) 30%,
        #a9a7b8 42%,
        var(--land) 52%,
        #b88a62 60%,
        var(--sea) 68%,
        var(--sea-deep) 100%);
  }
  .headline {
    position: absolute;
    left: 67px;
    top: 492px;
    font-weight: 700;
    font-size: 102px;
    line-height: 126px;
    letter-spacing: -1.5px;
  }
  .headline .dark { color: var(--navy); display: block; }
  .headline .accent { color: var(--cyan); display: block; }
  .brand {
    position: absolute;
    left: 57px;
    top: 1044px;
    width: 380px;
    height: 60px;
    display: flex;
    align-items: center;
    gap: 16px;
  }
  .brand-mark {
    flex: none;
    width: 60px; height: 60px;
    background: var(--copper);
  }
  .brand-name {
    font-weight: 700;
    font-size: 30px;
    letter-spacing: 2px;
    color: var(--copper);
    white-space: nowrap;
  }
  .website {
    position: absolute;
    left: 57px;
    top: 1136px;
    font-size: 33px;
    font-weight: 500;
    color: var(--light);
  }
  .contact {
    position: absolute;
    left: 494px;
    font-size: 23px;
    line-height: 31px;
    color: var(--light);
    display: flex;
    gap: 13px;
  }
  .contact.address { top: 1030px; }
  .contact.phone { top: 1140px; }
  .contact svg { flex: none; margin-top: 2px; }
</style>
</head>
<body>
  <main class="poster">
    <div class="hero-photo" role="img" aria-label="Photograph of the Monaco coastline: city buildings beneath a green mountain, turquoise sea and a soft cloudy sky"></div>

    <h1 class="headline">
      <span class="dark">Un nouveau</span>
      <span class="accent">regard sur</span>
      <span class="accent">l'immobilier</span>
    </h1>

    <div class="brand">
      <div class="brand-mark"></div>
      <span class="brand-name">BRUNOR AGENCY</span>
    </div>

    <div class="website">www.brunor-agency.com</div>

    <div class="contact address">
      <svg width="28" height="28" viewBox="0 0 28 28" aria-hidden="true">
        <circle cx="14" cy="14" r="14" fill="var(--icon-bg)"/>
        <path d="M7 14 L14 8 L21 14 M9 13 V20 H19 V13" fill="none" stroke="var(--navy)" stroke-width="2.2" stroke-linejoin="round"/>
        <rect x="12.5" y="15.5" width="3" height="4.5" fill="var(--navy)"/>
      </svg>
      <p>14 rue des Orvilles,<br>Passage Marcellin,<br>98 000 Monaco</p>
    </div>

    <div class="contact phone">
      <svg width="28" height="28" viewBox="0 0 28 28" aria-hidden="true">
        <circle cx="14" cy="14" r="14" fill="var(--icon-bg)"/>
        <path d="M10 7 L12.5 10.5 L11 12.5 C12 14.8 13.5 16.3 15.5 17 L17.5 15.5 L21 18 L19.5 21 C13 21 7 15 7 8.5 Z" fill="var(--navy)"/>
      </svg>
      <p>+377.93.48.25.71</p>
    </div>
  </main>
</body>
</html>
```